Real Estate Broker specializing in investment property needs business card

Would like to use a tag line for my company, Larkmoor Keys LLC (Right now I use Larkmoor Keys - For Real Estate Needs). I you have a more creative tag line it can be used because this is a new company.
We focus on Investment Acquisition Deals; Provide Custom Marketing Strategies for Sellers; Provide Pre Listinging Value Opportunities for Buyers.
Would like a call to action, but I do not want it to look too cluttered
I would like space to be available for writing on.
I prefer vertical business cards, but it could be horizontal on one or both sides. In fact if you can create a shape other than rectangle or a cut in the rectangle that makes it memorable, relevant to real estate, yet practical...(it will be kept) that would be of value.
If you have experience with business cards please feel free to suggest the paper type, size.

Target Market(s)

Investors, Neighbors, Friends... anyone who buys or would like to sell their residence

Industry/Entity Type

Real Estate

Contact Information for Business Card

The challenge is to incorporate a logo design of the Managing Brokerage Company, Tiller's Circle, and try to brand my company, LarkmoorKeys LLC. LarkmoorKeys LLC could work under another managing broker but the services and contact information would remain the same.

Font styles to use
Serif

Colors

Designer to choose colors to be used in the design.

Requirements
Must have
• Real estate company named Larkmoor Keys has to incorporate the logo of the managing broker company, Tillers Circle (see attached) into design of business card. (It is not a design for a logo I prefer but I need to use it. Size does not matter).
• Must also have my name, phone number and email address. (No website address yet)
• Just a few of the services we provide include
• We facilitate Investment Acquisition Deals; Provide Custom Marketing Strategies for Sellers; Provide Pre Listinging Value Opportunities for Buyers.
Nice to have
• Would like to use a tag line for my company, Larkmoor Keys LLC (Right now I use Larkmoor Keys - For Real Estate Needs). If you have a more creative tag line it can be used because this is a new company.
• Space to write information on, so they keep the card such as an appointment time to sit down and determine their needs
• A call to action maybe after the services? Or on the back of the card where it is blank.
• Larkmoor Keys does not have a logo, If you think a logo for Tillers Circle and a logo for LarkmoorKeys LLC can work, then please incorporate it into the business card.
Should not have
• Clutter
• Do not like comic style designs; prefer a sophisticated look and texture.

```html
<!DOCTYPE html>
<html lang="en">
<head>
<meta charset="utf-8">
<title>Larkmoor Keys – Business Card</title>
<link rel="stylesheet" href="https://fonts.googleapis.com/css2?family=Work+Sans:wght@400;500;600&display=swap">
<style>
  :root {
    --bg: #d9d9d9;
    --red: #b01a2e;
    --red-dark: #9c1426;
    --white: #ffffff;
    --gold: #f2a516;
    --ink: #333333;
    --rule: #b9b9b9;
  }
  * { box-sizing: border-box; margin: 0; padding: 0; }
  html, body { width: 1200px; height: 930px; overflow: hidden; }
  body {
    background: var(--bg);
    font-family: "Work Sans", sans-serif;
    position: relative;
  }
  .card {
    position: absolute;
    width: 740px;
    height: 423px;
    border-radius: 26px;
    overflow: hidden;
    box-shadow: 0 4px 14px rgba(0,0,0,0.18);
  }
  /* Back side */
  .card--back { left: 40px; top: 30px; background: var(--white); }
  .back__services {
    height: 190px;
    background: var(--red);
    color: var(--white);
    display: flex;
    flex-direction: column;
    justify-content: center;
    align-items: center;
    text-align: center;
    font-size: 19px;
    line-height: 1.55;
    letter-spacing: 0.3px;
  }
  .back__appointment {
    text-align: center;
    padding-top: 18px;
    font-size: 21px;
    color: var(--ink);
    letter-spacing: 0.5px;
  }
  .back__lines { margin: 14px 90px 0; }
  .back__line { height: 1px; background: var(--rule); margin-bottom: 34px; }
  .back__web {
    position: absolute;
    bottom: 22px;
    width: 100%;
    text-align: center;
    font-size: 15px;
    color: var(--ink);
    letter-spacing: 0.4px;
  }
  /* Front side */
  .card--front {
    left: 420px; top: 477px;
    background: linear-gradient(100deg, var(--red-dark), var(--red) 45%, var(--red-dark));
    color: var(--white);
  }
  .front__broker {
    position: absolute;
    left: 46px; top: 62px;
    display: flex; align-items: center; gap: 12px;
    font-size: 30px; font-weight: 500;
    color: var(--gold);
  }
  .front__broker-dot { width: 16px; height: 16px; border-radius: 50%; background: var(--gold); }
  .front__identity { position: absolute; right: 46px; top: 54px; text-align: right; }
  .front__name { font-size: 28px; font-weight: 600; color: var(--gold); letter-spacing: 0.5px; }
  .front__title { font-size: 17px; margin-top: 2px; }
  .front__rule { position: absolute; left: 40px; right: 40px; top: 170px; height: 1px; background: rgba(255,255,255,0.85); }
  .front__address {
    position: absolute; right: 46px; top: 196px;
    text-align: right; font-size: 17px; line-height: 1.45;
  }
  .front__contacts {
    position: absolute; left: 46px; bottom: 34px;
    list-style: none; font-size: 19px; line-height: 1.4;
  }
  .front__contacts li { display: flex; align-items: center; gap: 12px; }
  .front__contacts svg { width: 14px; height: 14px; flex: none; }
</style>
</head>
<body>

<section class="card card--back">
  <div class="back__services">
    <p>We facilitate Investment Acquisition Deals</p>
    <p>Provide Custom Marketing Strategies for Sellers</p>
    <p>Provide Pre Listinging Value Opportunities for Buyers.</p>
  </div>
  <p class="back__appointment">Appointment</p>
  <div class="back__lines">
    <div class="back__line"></div>
    <div class="back__line"></div>
    <div class="back__line"></div>
  </div>
  <p class="back__web">www.larkmoorhomes.com</p>
</section>

<section class="card card--front">
  <div class="front__broker"><span class="front__broker-dot"></span>Tillers Circle</div>
  <div class="front__identity">
    <p class="front__name">DARREN HOLLOWAY</p>
    <p class="front__title">Director</p>
  </div>
  <div class="front__rule"></div>
  <p class="front__address">1480 Fernhill Ave<br>Suite 200 B<br>Brightvale, CO 80999</p>
  <ul class="front__contacts">
    <li><svg viewBox="0 0 16 16"><path fill="#f2a516" d="M3 1l3 3-2 2c1 2 3 4 5 5l2-2 3 3-2 3C7 15 1 9 1 3z"/></svg>(555) 214-0387</li>
    <li><svg viewBox="0 0 16 16"><rect x="4" y="1" width="8" height="14" rx="1.5" fill="#f2a516"/><rect x="5.5" y="3" width="5" height="8" fill="#b01a2e"/></svg>(555) 630-1942</li>
    <li><svg viewBox="0 0 16 16"><rect x="1" y="3" width="14" height="10" fill="none" stroke="#f2a516" stroke-width="1.6"/><path d="M1 3l7 6 7-6" fill="none" stroke="#f2a516" stroke-width="1.6"/></svg>info@larkmoorhomes.com</li>
    <li><svg viewBox="0 0 16 16"><circle cx="8" cy="8" r="6.5" fill="none" stroke="#f2a516" stroke-width="1.4"/><ellipse cx="8" cy="8" rx="3" ry="6.5" fill="none" stroke="#f2a516" stroke-width="1.2"/><path d="M1.5 8h13" stroke="#f2a516" stroke-width="1.2"/></svg>www.larkmoorhomes.com</li>
  </ul>
</section>

</body>
</html>
```